Brochure for dog daycare and boarding center

Looking for a multi page brochure for my dog daycare, overnight care, and Traing facility.

Content to be taken from our current website. pawmeadowhub.com

Brochure should be professional yet personable with stock images of dogs playing and having fun.

Here are the different sections to include for content which can all be found on our website at: pawmedowhub.com

Highlight our three main services: Daycare, Boarding, Training

Why Doggie Daycare?
Drop your dog off at Bright Lanes and let them spend the day socializing with other dogs, running around and burning off all that energy! That way, an evening in your home is relaxing for both you and your pooped out pooch!

Benefits:
1.) Playing with other dogs will help your pooch expend pent up
energy!
2.) Individual attention & personalized care from our well-trained staff.
3.) Interaction with other dogs help to build positive social behavior.
Increased confidence and agility.
4.) Provides exercise for your dog & prevents obesity.
5.) Peace of mind that your dog is safe and happy while you are away
during the day.

Daycare is $20 for a full day and $15 for half day, as well as packages.

Boarding:
When boarding at Bright Lanes, your dog will enjoy playing with other dogs and then retire to the bedroom for a good night sleep. We offer climate controlled boarding rooms that will insure your dog gets a good nights sleep.
Boarding starts at $40 a night with discounts for multiple dogs and small dogs

Training:
Let your dog live and learn from us! Your dog is invited to stay at Bright lanes up to six weeks. During that time we will work daily with your dog on basic training skills. At our facility, we will use both training and intermediate training, teaching your dog everything from sit-stays, down-stays to place bed, heeling and name recognition. Afterward, we will show you how to continue the training to provide your dog with a seamless transition home and make his stay at Bright Lanes worth it. Board and Train price: $1500 for 6 weeks.

Make sure to include: phone number, web address, e-mail address, mailing address, Hours

Monday 7:00 AM - 5:30 PM
Tuesday 7:00 AM - 5:30 PM
Wednesday 7:00 AM - 5:30 PM
Thursday 7:00 AM - 5:30 PM
Friday 7:00 AM - 5:30 PM
Saturday 9:00 AM - 5:30 PM
Sunday 8:00 AM - 10:00 AM & 4:30 PM - 7:30 PM

Also we would like a social media section that has snapchat (will get you a picture), facebook, and a place for us to say something about our mobile app (will find a qr code for this).

Target Market(s)

dog owners in the Cedar Falls Waterloo area

Industry/Entity Type

Pet Care

Font styles to use
Serif

Colors
fbee3d
ffffff
5c5c5c

Requirements
Must have
• Clean is better then cluttered.
Should not have
• An over use of paw prints and bones (some are ok)

```html
<!DOCTYPE html>
<html lang="en">
<head>
<meta charset="utf-8">
<title>Bright Lanes – Daycare, Boarding, Training Brochure</title>
<link href="https://fonts.googleapis.com/css2?family=Open+Sans:ital,wght@0,400;0,600;0,700;1,600;1,700&family=Archivo:ital,wght@1,800&family=EB+Garamond:wght@400&display=swap" rel="stylesheet">
<style>
  :root{
    --backdrop:#8a5c3c;
    --paper:#ffffff;
    --green:#8cc63f;
    --green-dark:#4e8a1a;
    --charcoal:#333333;
    --slate:#5c5c5c;
    --mist:#e6e6e6;
    --ink:#222222;
  }
  *{box-sizing:border-box;margin:0;padding:0}
  html,body{width:1200px;height:842px;overflow:hidden;background:var(--backdrop)}
  body{position:relative;font-family:"Open Sans",Arial,sans-serif;color:var(--ink)}

  .page{position:absolute;top:58px;width:528px;height:740px;background:var(--paper);overflow:hidden}
  .page--services{left:54px}
  .page--daycare{left:608px}

  .photo{position:absolute}
  .box{position:absolute}

  /* ---- Services page ---- */
  .photo--tunnel{left:0;top:0;width:200px;height:124px;background:linear-gradient(160deg,#9aa8b4,#7fa050 60%,#d86a3a)}
  .photo--hoop{left:200px;top:0;width:126px;height:124px;background:radial-gradient(circle at 50% 55%,#d8a860 30%,#c8283a 58%,#e9ecef 75%)}
  .strip-bar{position:absolute;left:0;top:124px;width:326px;height:21px;background:#111}
  .photo--jump{left:326px;top:0;width:202px;height:145px;background:linear-gradient(180deg,#dfe4e6,#b8c2b0 45%,#6e9a3c)}
  .photo--hug{left:30px;top:150px;width:230px;height:142px;background:linear-gradient(100deg,#d9a45a,#f0e2cf 55%,#f4f4f4)}

  .box--green{background:var(--green);color:var(--ink)}
  .box--boarding{left:264px;top:150px;width:229px;height:142px;padding:6px 10px}
  .box--training{left:30px;top:296px;width:230px;height:190px;padding:6px 16px}
  .box h2{font-weight:600;font-size:16px;margin-bottom:8px}
  .box p.body{font-size:7.6px;line-height:1.5;text-align:justify}
  .box p.price{font-weight:600;font-size:11px;line-height:1.35;margin-top:6px}

  .box--hours{left:264px;top:296px;width:229px;height:190px;background:var(--charcoal);color:#fff;padding:6px 18px;overflow:hidden}
  .hours{border-collapse:collapse;font-size:10.2px;font-weight:600;line-height:1.25}
  .hours td{padding:1.5px 0;vertical-align:top}
  .hours td:first-child{width:71px}
  .contact-label{margin-top:8px;text-align:center;color:var(--green);font-weight:600;font-size:13px;line-height:1.25}
  .contact-phone{text-align:center;color:var(--green);font-weight:600;font-size:23px;line-height:1.1}
  .address--services{position:absolute;left:264px;top:490px;width:229px;text-align:center;font-size:7.6px}

  .photo--pups{left:20px;top:500px;width:400px;height:188px;background:radial-gradient(ellipse at 55% 55%,#d9dde0 0%,#f6f6f6 70%,#fff 100%)}
  .photo--girl-dog{left:360px;top:516px;width:168px;height:172px;background:linear-gradient(200deg,#c8a0d8,#d9a85a 60%,#f5f0e8)}
  .brand{position:absolute;display:flex;align-items:center;gap:6px;font-weight:700;color:var(--ink)}
  .brand .mark{width:12px;height:12px;background:var(--green)}
  .brand--services{left:34px;top:566px;font-size:18px}

  .footer-web{position:absolute;left:0;top:688px;width:528px;height:52px;background:var(--green);text-align:center;font-weight:700;font-size:24px;letter-spacing:2.2px;line-height:52px;color:#111}

  /* ---- Daycare page ---- */
  .brand--daycare{left:32px;top:88px;font-size:20px}
  .header-band{position:absolute;left:0;top:0}
  .tagline{position:absolute;left:246px;top:30px;font-family:"EB Garamond",Georgia,serif;font-size:19px;line-height:1.25;color:var(--ink)}
  .services{position:absolute;left:208px;top:82px;list-style:none}
  .services li{display:flex;align-items:center;font-family:"Archivo",Arial,sans-serif;font-style:italic;font-weight:800;font-size:34px;line-height:34px;color:#fff}
  .services li::before{content:"";width:0;height:0;border-top:8px solid transparent;border-bottom:8px solid transparent;border-left:10px solid #111;margin-right:6px}
  .services li:nth-child(1){margin-left:28px}
  .services li:nth-child(2){margin-left:14px}

  .photo--woman-puppy{left:0;top:126px;width:164px;height:254px;background:linear-gradient(180deg,#7a4a2a 0%,#f0d4c0 30%,#e86aa0 60%,#f3efe6)}
  .photo--grass{left:116px;top:204px;width:388px;height:176px;background:linear-gradient(140deg,#4f8a2a,#7cb24a 50%,#f3e9dc);clip-path:polygon(18% 0,100% 0,82% 100%,0 100%)}

  .photo--ball{left:68px;top:384px;width:270px;height:122px;background:linear-gradient(110deg,#e9d8b0,#8bbf55 50%,#d98c3a);clip-path:polygon(16% 0,100% 0,92% 100%,0 100%)}
  .why{position:absolute;left:296px;top:384px;width:232px;height:122px;background:var(--charcoal);color:#fff;clip-path:polygon(16% 0,100% 0,100% 100%,0 100%);padding:10px 10px 0 30px}
  .why h2{font-weight:600;font-size:16px;line-height:1.25;margin-left:12px;margin-bottom:6px}
  .why p{font-size:7.2px;line-height:1.45;text-align:center}

  .photo--basket{left:48px;top:512px;width:148px;height:92px;background:radial-gradient(ellipse at 50% 65%,#b0783a 25%,#e8dccb 55%,#fff 80%)}
  .benefits{position:absolute;left:212px;top:514px;width:310px}
  .benefits h3{color:var(--green);font-weight:700;font-size:12px;margin-left:14px;margin-bottom:3px}
  .benefits ol{list-style:none;counter-reset:b}
  .benefits li{counter-increment:b;position:relative;padding-left:14px;font-size:7px;line-height:1.45;margin-bottom:3px}
  .benefits li::before{content:counter(b);position:absolute;left:0;top:0;width:9px;height:9px;border-radius:50%;background:var(--green);color:#fff;font-size:6px;font-weight:700;text-align:center;line-height:9px}
  .benefits li:nth-child(1){margin-left:10px}
  .benefits li:nth-child(2){margin-left:6px}
  .benefits li:nth-child(3){margin-left:2px}
  .benefits li:nth-child(4){margin-left:-6px}
  .benefits li:nth-child(5){margin-left:-10px}

  .rate{position:absolute;left:36px;top:618px;color:var(--green-dark);font-style:italic;font-weight:700;line-height:1.15}
  .rate .lead{font-size:18px;letter-spacing:-.3px}
  .rate .tail{font-size:13px}

  .footer-band{position:absolute;left:0;top:670px;width:528px;height:44px;background:var(--mist)}
  .footer-phone{position:absolute;left:24px;top:670px;width:212px;height:44px;background:var(--green);clip-path:polygon(12% 0,100% 0,88% 100%,0 100%);font-weight:700;font-size:25px;line-height:44px;text-align:center;color:#111}
  .footer-info{position:absolute;left:262px;top:674px;width:250px;text-align:center}
  .footer-info .address{font-weight:700;font-size:8.4px;margin-bottom:5px}
  .footer-info .email{font-style:italic;font-weight:600;font-size:11px;color:var(--slate)}
  .footer-info .email span{color:var(--green-dark)}
</style>
</head>
<body>

<section class="page page--services" aria-label="Services page">
  <div class="photo photo--tunnel" role="img" aria-label="Photo: small dog running through a striped agility tunnel beside its handler"></div>
  <div class="photo photo--hoop" role="img" aria-label="Photo: golden retriever leaping through a red agility hoop"></div>
  <div class="strip-bar"></div>
  <div class="photo photo--jump" role="img" aria-label="Photo: husky clearing an agility jump while a trainer watches"></div>

  <div class="photo photo--hug" role="img" aria-label="Photo: girl hugging a golden retriever"></div>

  <div class="box box--green box--boarding">
    <h2>Boarding:</h2>
    <p class="body">When boarding at Bright Lanes, your dog will enjoy playing with other dogs and then retire to the bedroom for a good night sleep. We offer climate controlled boarding rooms that will insure your dog gets a good nights sleep.</p>
    <p class="price">Boarding starts at $40 a night with discounts for multiple dogs and small dogs</p>
  </div>

  <div class="box box--green box--training">
    <h2>Training:</h2>
    <p class="body">Let your dog live and learn from us! Your dog is invited to stay at Bright lanes up to six weeks. During that time we will work daily with your dog on basic training skills. At our facility, we will use both training and intermediate training, teaching your dog everything from sit-stays, down-stays to place bed, heeling and name recognition. Afterward, we will show you how to continue the training to provide your dog with a seamless transition home and make his stay at Bright Lanes worth it.</p>
    <p class="price">Board and Train price: $1500 for 6 weeks.</p>
  </div>

  <div class="box box--hours">
    <table class="hours">
      <tr><td>Monday</td><td>7:00 AM - 5:30 PM</td></tr>
      <tr><td>Tuesday</td><td>7:00 AM - 5:30 PM</td></tr>
      <tr><td>Wednesday</td><td>7:00 AM - 5:30 PM</td></tr>
      <tr><td>Thursday</td><td>7:00 AM - 5:30 PM</td></tr>
      <tr><td>Friday</td><td>7:00 AM - 5:30 PM</td></tr>
      <tr><td>Saturday</td><td>9:00 AM - 5:30 PM</td></tr>
      <tr><td>Sunday</td><td>8:00 AM - 10:00 AM &amp;<br>4:30 PM - 7:30 PM</td></tr>
    </table>
    <p class="contact-label">Contact Us:</p>
    <p class="contact-phone">319-555-0142</p>
  </div>
  <p class="address--services">2260 Willow Bend Drive Cedar Falls IA, 50613</p>

  <div class="photo photo--pups" role="img" aria-label="Photo: border collie lying down and a Boston terrier puppy standing"></div>
  <div class="photo photo--girl-dog" role="img" aria-label="Photo: smiling girl lying beside a golden retriever with a toy"></div>
  <div class="brand brand--services"><span class="mark"></span>Bright Lanes</div>

  <div class="footer-web">www.PawMeadowHub.com</div>
</section>

<section class="page page--daycare" aria-label="Daycare page">
  <svg class="header-band" width="528" height="666" viewBox="0 0 528 666" aria-hidden="true">
    <polygon points="240,24 528,24 528,60 508,202 180,202" fill="var(--green)"/>
    <polygon points="0,380 110,380 0,666" fill="var(--green)"/>
  </svg>
  <div class="brand brand--daycare"><span class="mark"></span>Bright Lanes</div>
  <p class="tagline">Dog daycare, Overnight care,<br>and Traing facility</p>
  <ul class="services">
    <li>DAYCARE</li>
    <li>BOARDING</li>
    <li>TRAINING</li>
  </ul>

  <div class="photo photo--woman-puppy" role="img" aria-label="Photo: young woman holding a white Labrador puppy"></div>
  <div class="photo photo--grass" role="img" aria-label="Photo: two terrier puppies playing on their backs in the grass"></div>

  <div class="photo photo--ball" role="img" aria-label="Photo: Labrador puppy with a tennis ball and a puppy chasing a football"></div>
  <div class="why">
    <h2>Why Doggie<br>Daycare?</h2>
    <p>Drop your dog off at Bright Lanes and let them spend the day socializing with other dogs, running around and burning off all that energy! That way, an evening in your home is relaxing for both you and your pooped out pooch!</p>
  </div>

  <div class="photo photo--basket" role="img" aria-label="Photo: two puppies sleeping in a wicker basket"></div>
  <div class="benefits">
    <h3>Benefits:</h3>
    <ol>
      <li>Playing with other dogs will help your pooch expend pent up energy!</li>
      <li>Individual attention &amp; personalized care from our well-trained staff.</li>
      <li>Interaction with other dogs help to build positive social behavior.<br>Increased confidence and agility.</li>
      <li>Provides exercise for your dog &amp; prevents obesity.</li>
      <li>Peace of mind that your dog is safe and happy while you are away during the day.</li>
    </ol>
  </div>

  <p class="rate"><span class="lead">Daycare is $20 for a full day and $15 for half day,</span><br><span class="tail">as well as packages.</span></p>

  <div class="footer-band"></div>
  <div class="footer-phone">319-555-0142</div>
  <div class="footer-info">
    <p class="address">2260 Willow Bend Drive Cedar Falls IA, 50613</p>
    <p class="email">email: <span>hello@pawmeadowhub.com</span></p>
  </div>
</section>

</body>
</html>
```